Environmentally conscious Waste Management Company requires business card

We Require a Business card for our environmentally conscious waste management company . The business card should have a very clean design. be double sided and incorporate our logo..
The card will need o have 9 lines for the contact details - that are
Name
Title
Business
Address Line 1
Address Line 2
Address Line 3
Phone
Mobile
Email

Industry/Entity Type

Waste Management

Font styles to use
Other font styles liked:
• Helvetica or similar

```html
<!DOCTYPE html>
<html lang="en">
<head>
<meta charset="utf-8">
<title>clearcycle – business card</title>
<link rel="stylesheet" href="https://fonts.googleapis.com/css2?family=Inter:wght@300;400&display=swap">
<style>
  :root {
    --green: #1fc232;
    --ink: #3a3a3a;
    --ink-soft: #5a5a5a;
    --paper: #ffffff;
    --backdrop: #2b2b2b;
  }
  * { box-sizing: border-box; margin: 0; padding: 0; }
  html, body {
    width: 1200px; height: 900px; overflow: hidden;
    background: var(--backdrop);
    font-family: "Inter", "Helvetica Neue", Arial, sans-serif;
  }
  .sheet {
    width: 1200px; height: 900px;
    display: flex; align-items: center; justify-content: center; gap: 40px;
  }
  .card {
    position: relative;
    width: 560px; height: 320px;
    background: var(--paper);
    overflow: hidden;
    box-shadow: 0 8px 24px rgba(0,0,0,.45);
  }
  .card-bands { position: absolute; inset: 0; }
  .card-bands path { fill: var(--green); }

  .brand {
    position: absolute;
    color: var(--ink);
    font-weight: 400;
    text-transform: uppercase;
    letter-spacing: 0.28em;
    line-height: 1;
    white-space: nowrap;
  }
  .card--front .brand { left: 50%; top: 50%; transform: translate(-50%, -50%); font-size: 34px; }
  .card--back .brand { left: 34px; top: 64px; font-size: 24px; }

  .person { position: absolute; right: 30px; top: 40px; text-align: right; color: var(--ink); font-weight: 300; }
  .person-name { font-size: 22px; letter-spacing: 0.01em; }
  .person-title { font-size: 13px; color: var(--ink-soft); margin-top: 1px; }

  .contact-list { position: absolute; list-style: none; font-size: 12px; color: var(--ink); font-weight: 300; }
  .contact-list li { display: flex; align-items: center; gap: 10px; height: 24px; }
  .contact-list svg { width: 18px; height: 18px; flex: none; }
  .contact-list svg * { fill: none; stroke: var(--green); stroke-width: 1.6; stroke-linejoin: round; }

  .social { right: 40px; top: 120px; }
  .social .marker { width: 14px; height: 14px; background: var(--green); border-radius: 50%; flex: none; }

  .direct { left: 34px; top: 184px; }

  .address {
    position: absolute; left: 190px; bottom: 30px;
    display: flex; align-items: center; gap: 8px;
    font-size: 12px; color: var(--ink); font-weight: 300;
  }
  .address svg { width: 16px; height: 20px; }
  .address svg path { fill: var(--green); }
  .address svg circle { fill: var(--paper); }
</style>
</head>
<body>
<main class="sheet">

  <section class="card card--front" aria-label="Card front">
    <svg class="card-bands" viewBox="0 0 560 320" aria-hidden="true">
      <path d="M0 0 H560 V0 C540 0 530 8 505 8 H0 Z"/>
      <path d="M560 0 H470 C500 0 505 10 530 10 H560 Z"/>
      <path d="M0 320 H560 V310 H0 Z"/>
    </svg>
    <p class="brand">clearcycle</p>
  </section>

  <section class="card card--back" aria-label="Card back">
    <svg class="card-bands" viewBox="0 0 560 320" aria-hidden="true">
      <path d="M0 0 H420 C398 0 392 10 368 10 H0 Z"/>
      <path d="M560 320 H140 C165 320 172 308 196 308 H560 Z"/>
    </svg>

    <p class="brand">clearcycle</p>

    <div class="person">
      <p class="person-name">YOUR NAME</p>
      <p class="person-title">Designation</p>
    </div>

    <ul class="contact-list social">
      <li><span class="marker"></span>@clearcyclenz</li>
      <li><span class="marker"></span>/clearcycle.co.nz</li>
      <li><span class="marker"></span>/in-4KrP</li>
    </ul>

    <ul class="contact-list direct">
      <li>
        <svg viewBox="0 0 20 20" aria-hidden="true"><path d="M3 7 C3 4 17 4 17 7 L15 8 L13 7 V6 H7 V7 L5 8 Z"/><path d="M5 10 H15 L16 16 H4 Z"/><circle cx="10" cy="13" r="1.5"/></svg>
        00(64)3550172
      </li>
      <li>
        <svg viewBox="0 0 20 20" aria-hidden="true"><rect x="6" y="2" width="8" height="16" rx="1.5"/><path d="M9 15.5 H11"/></svg>
        00(64)227430915
      </li>
      <li>
        <svg viewBox="0 0 20 20" aria-hidden="true"><rect x="2" y="5" width="16" height="11"/><path d="M2 5 L10 11 L18 5"/></svg>
        marenholt@clearcycle.com
      </li>
    </ul>

    <p class="address">
      <svg viewBox="0 0 16 20" aria-hidden="true"><path d="M8 0 C3.6 0 0 3.4 0 7.6 C0 13 8 20 8 20 C8 20 16 13 16 7.6 C16 3.4 12.4 0 8 0 Z"/><circle cx="8" cy="7.5" r="3"/></svg>
      Kowhai Lane, Taupo, New Zealand 3330
    </p>
  </section>

</main>
</body>
</html>
```